BrightHearth Flyer

A simple flyer that gets people attention
I have a attached a sample of what we use now and a picture we use
We service gas fireplaces and need a eye catching but not to cluttered flyer to promote our business. the cost per fireplace should be $60.00
Updates

Project Deadline Extended
Reason: Sorry for the delay We are out of town on holidays with sketchy internet service To frustrating to complete this project till I am back in a week Thank you for your patience Kind regards Dale

```html
<!DOCTYPE html>
<html lang="en">
<head>
<meta charset="utf-8">
<title>BrightHearth Gas Services – Notice to Owners</title>
<link rel="stylesheet" href="https://fonts.googleapis.com/css2?family=Arimo:wght@400;700&family=Fredoka:wght@600&display=swap">
<style>
  :root {
    --page-bg: #ece7e1;
    --sheet: #f7f7f7;
    --band: #ebebeb;
    --column: #dcdcdc;
    --red: #9c1015;
    --red-bright: #a8191c;
    --red-dark: #6e0b0b;
    --text-red: #8c1414;
    --title-red: #8f1414;
    --panel: rgba(72, 30, 30, 0.9);
    --white: #ffffff;
  }
  * { margin: 0; padding: 0; box-sizing: border-box; }
  html, body { width: 1000px; height: 1200px; overflow: hidden; }
  body { background: var(--page-bg); position: relative; font-family: "Arimo", Arial, sans-serif; }

  .flyer {
    position: absolute; left: 195px; top: 205px;
    width: 612px; height: 792px;
    background: var(--sheet);
    overflow: hidden;
  }
  .flyer__band { position: absolute; left: 0; top: 0; width: 612px; height: 92px; background: var(--band); }
  .flyer__column { position: absolute; left: 25px; top: 0; width: 253px; height: 502px; background: var(--column); }
  .block { position: absolute; }
  .block--bright { left: 441px; top: 0; width: 71px; height: 72px; background: var(--red-bright); }
  .block--dark { left: 512px; top: 0; width: 100px; height: 98px; background: var(--red-dark); }
  .block--mid { left: 539px; top: 98px; width: 73px; height: 72px; background: var(--red); }

  .flyer__title {
    position: absolute; left: 38px; top: 29px;
    font-family: "Fredoka", "Arial Rounded MT Bold", sans-serif;
    font-weight: 600; font-size: 19px; line-height: 24px;
    color: var(--title-red); letter-spacing: 0.1px;
  }

  .flyer__body {
    position: absolute; left: 28px; top: 113px;
    color: var(--text-red); font-size: 14px; line-height: 16.6px;
  }
  .flyer__body p { margin-bottom: 9.5px; white-space: nowrap; }

  .photo {
    position: absolute; left: 0; top: 502px; width: 429px; height: 290px;
    background:
      radial-gradient(ellipse 70px 60px at 215px 90px, rgba(242,150,40,0.85), rgba(180,70,20,0) 100%),
      radial-gradient(ellipse 160px 90px at 150px 230px, rgba(225,170,150,0.55), rgba(0,0,0,0) 100%),
      linear-gradient(180deg, #3a2a24 0%, #241a18 45%, #2b2326 100%);
  }
  .flyer__accent { position: absolute; left: 429px; top: 502px; width: 183px; height: 290px; background: var(--red); }

  .info {
    position: absolute; left: 252px; top: 520px; width: 360px; height: 202px;
    background: var(--panel);
    color: var(--white); font-size: 14px; line-height: 16.6px;
    padding: 8px 10px 0 16px;
    white-space: nowrap;
  }
  .info p { margin-bottom: 14px; }
  .info .contact { padding-left: 3px; }
  .info .email { font-weight: 700; }
</style>
</head>
<body>
  <main class="flyer">
    <div class="flyer__band"></div>
    <div class="flyer__column"></div>
    <div class="block block--bright"></div>
    <div class="block block--dark"></div>
    <div class="block block--mid"></div>

    <h1 class="flyer__title">NOTICE TO THE OWNERS<br>NAME OF PROPERTY</h1>

    <section class="flyer__body">
      <p>BRIGHTHEARTH GAS SERVICES will be on site conducting gas fireplace safety<br>inspections and maintenance for NAME OF PROPERTY on DATE OF SERVICE.<br>If you wish to have your fireplace serviced, please put your name and unit<br>number on the sign-up sheet provided. We will require approximately 20 -<br>30 minutes to service each fireplace and require that the fireplace is cool to<br>conduct the work. Please do not use your fireplace within 2 hours of your<br>appointment as we do not want the technicians to receive burns.</p>
      <p>The National Home Energy Office states that all fireplaces<br>require regular servicing. Fireplace manufacturers recommend each unit be serviced<br>annually by a qualified technician and insurance companies and Fire Departments are<br>now asking for reports regarding fireplace safety inspections and servicing. The service<br>BrightHearth Gas Services will provide will entail a thorough assessment of pilot, burner and<br>valve operation, a door seal inspection, an inspection of the electrical circuits,<br>repositioning of the logs, cleaning and adjustment of fan and controls, cleaning of the<br>firebox and glass, a carbon monoxide test, testing of fittings for gas leaks and a<br>complete operational test once the service is complete.</p>
      <p>Possible indication that your gas fireplace requires service include: (1) Cloudy film on<br>glass, (2) Strong odors when fireplace is in operation, (3) Soot build up on glass, logs or<br>exterior of building, (4) Tarnished/discolored brass, (5) Pilot light outages, (6) Main<br>burner is not lighting consistently, (7) Delayed ignition, and (8) Flames are not evenly<br>dispersed.</p>
    </section>

    <div class="photo" role="img" aria-label="Photo of a family warming their bare feet in front of a lit gas fireplace"></div>
    <div class="flyer__accent"></div>

    <section class="info">
      <p>The cost is $60.00 (tax included)<br>(Owners must have payment ready at time of<br>inspection.<br>Payment may be made in the form of cash, cheque,<br>credit card)</p>
      <p class="contact">For further information please contact Nadia at:<br>BrightHearth Gas Services 604.555.0187</p>
      <p class="contact">You may also email us at:<br><span class="email">nadia.brighthearth@example.com</span></p>
    </section>
  </main>
</body>
</html>
```